IT Service Provider

We need a website which reflects the IT Services we can offer to small and mid-size companies. This reaches from LAN/WAN, Security, VoIP, WiFi, Storage, Penetration testing.and Support.

In addition to that, a Logo is needed and should be embedded in the website.

Company is registered in the UK under:
Pellwick Ltd
Company No. 05927318

Industry/Entity Type

Security

```html
<!DOCTYPE html>
<html lang="en">
<head>
<meta charset="utf-8">
<title>Pellwick – LAN/WAN &amp; IT Services</title>
<link href="https://fonts.googleapis.com/css2?family=Mulish:wght@300;400;600;700&display=swap" rel="stylesheet">
<style>
:root{
  --navy:#1d2c63;
  --blue:#1f8ad8;
  --blue-dark:#1c4fa0;
  --text:#6b6b6b;
  --heading:#333;
  --white:#fff;
  --footer:#1c2a5a;
  --band:#e4e6ea;
}
*{margin:0;padding:0;box-sizing:border-box}
html,body{width:736px;height:1200px;overflow:hidden;background:var(--white)}
body{font-family:"Mulish",sans-serif;position:relative;color:var(--text)}
.site-header{position:absolute;top:0;left:0;width:736px;height:58px;background:var(--white)}
.brand{position:absolute;left:94px;top:16px;display:flex;align-items:center;gap:6px}
.brand-dot{width:10px;height:10px;border-radius:50%;background:var(--blue)}
.brand-name{font-size:20px;font-weight:600;color:var(--blue-dark);letter-spacing:.2px}
.main-nav{position:absolute;top:27px;left:346px;display:flex;gap:20px;font-size:10px;color:#555}
.main-nav a{color:inherit;text-decoration:none}
.main-nav a.active{color:var(--blue-dark)}
.hero{position:absolute;top:58px;left:0;width:736px;height:312px;background:linear-gradient(100deg,#3a3c40 0%,#8e9298 35%,#c9cbcf 55%,#6e7278 80%,#4a4d52 100%)}
.hero-box{position:absolute;left:88px;top:105px;width:293px;height:109px;background:rgba(30,135,215,.92);padding:20px 20px;color:var(--white)}
.hero-box h1{font-size:21px;font-weight:400;letter-spacing:.2px}
.hero-box h2{font-size:11px;font-weight:400;margin-top:4px;letter-spacing:.3px}
.hero-box p{font-size:6.6px;line-height:11px;margin-top:6px}
.hero-dots{position:absolute;left:366px;top:297px;display:flex;gap:3px}
.hero-dots span{width:6px;height:6px;border-radius:50%;background:rgba(255,255,255,.7)}
.hero-dots span:first-child{background:#fff}
.intro{position:absolute;top:370px;left:0;width:736px;text-align:center}
.intro h2{margin-top:24px;font-size:20px;font-weight:400;color:var(--navy)}
.intro h3{font-size:13px;font-weight:400;color:var(--blue-dark);margin-top:2px}
.intro p{font-size:6.8px;line-height:12px;margin:10px auto 0;width:560px}
.intro p+p{margin-top:2px}
.btn{display:inline-block;margin-top:14px;background:var(--blue-dark);color:var(--white);font-size:8px;font-weight:600;padding:5px 12px;border-radius:2px;text-decoration:none}
.services{position:absolute;top:532px;left:0;width:736px;height:218px;background:linear-gradient(90deg,#d9dce1,#f1f2f4 50%,#d6d9de)}
.services h2{text-align:center;font-size:18px;font-weight:400;color:#222;margin-top:30px}
.service{position:absolute;top:71px;width:130px;text-align:center}
.service .icon{width:56px;height:56px;margin:0 auto;border-radius:50%;background:var(--blue);border:2px solid #fff;display:flex;align-items:center;justify-content:center}
.service h3{font-size:11.5px;font-weight:400;color:var(--blue);margin-top:5px}
.service p{font-size:6.6px;line-height:11px;margin-top:2px}
.cards .card{position:absolute;top:778px;width:165px}
.card .photo{width:165px;height:72px}
.card h3{font-size:13px;font-weight:400;color:var(--heading);margin-top:11px}
.card p{font-size:6.6px;line-height:12px;margin-top:3px}
.map{position:absolute;top:954px;left:0;width:736px;height:176px;background:linear-gradient(90deg,#e8e4d8,#ece8dd 40%,#e6e2d6)}
.address{position:absolute;left:252px;top:993px;width:115px;height:53px;background:var(--white);font-size:6.6px;line-height:11px;text-align:center;padding-top:4px;color:#333;box-shadow:0 1px 3px rgba(0,0,0,.2)}
.pin{position:absolute;left:303px;top:1058px}
.site-footer{position:absolute;top:1130px;left:0;width:736px;height:70px;background:var(--footer);color:#dfe3ee}
.footer-nav{position:absolute;left:97px;top:22px;font-size:8px}
.footer-nav a{color:inherit;text-decoration:none}
.copyright{position:absolute;left:97px;top:40px;font-size:6.6px;color:#aeb6cc}
.social{position:absolute;left:598px;top:16px;display:flex;gap:6px}
.social span{width:14px;height:14px;border-radius:2px;background:#3d7fd0}
</style>
</head>
<body>
<header class="site-header">
  <div class="brand"><span class="brand-dot"></span><span class="brand-name">Pellwick</span></div>
  <nav class="main-nav">
    <a class="active" href="#">HOME</a><a href="#">ABOUT US</a><a href="#">SERVICES</a><a href="#">PROJECTS</a><a href="#">CONTACT</a>
  </nav>
</header>

<section class="hero" role="img" aria-label="Photo of a businessman touching a glowing network diagram">
  <div class="hero-box">
    <h1>LAN/WAN &amp; IT SERVICES</h1>
    <h2>MORBI DIAM MAURIS VIVERRA GRAVIDA</h2>
    <p>Malesuada nec ultricies sit amet porttitor mattis enim in massa<br>libero interdum nec interdum vel blandit sed nulla</p>
  </div>
  <div class="hero-dots"><span></span><span></span><span></span><span></span></div>
</section>

<section class="intro">
  <h2>Curabitur vel amet magna malesuada ultrices</h2>
  <h3>Lorem ipsum dolor sit amet consectetuer adipiscing</h3>
  <p>Phasellus pellentesque aliquam enim Proin dui lectus cursus eu mattis laoreet viverra sit amet quam Curabitur vel dolor ultrices ipsum</p>
  <p>Curabitur vel mi sit amet magna malesuada ultrices Ut nisi erat fermentum vel congue id euismod in elit Fusce ultricies orci ac feugiat suscipit leo massa sodales velit et scelerisque mi tortor at ipsum Proin orci odio commodo ac gravida non tristique vel tellus Pellentesque nibh</p>
  <a class="btn" href="#">READ MORE</a>
</section>

<section class="services">
  <h2>Services Provides</h2>
  <div class="service" style="left:94px">
    <div class="icon"><svg width="28" height="28" viewBox="0 0 28 28" fill="none" stroke="#fff" stroke-width="2"><rect x="6" y="5" width="16" height="12" rx="1"/><line x1="14" y1="17" x2="14" y2="21"/><line x1="5" y1="23" x2="23" y2="23"/><line x1="14" y1="21" x2="14" y2="23"/></svg></div>
    <h3>LAN/WAN</h3>
    <p>Morbi diam mauris viverra in gravida<br>eu mattis in ante Morbi eget arcu<br>Morbi porta libero ullam</p>
  </div>
  <div class="service" style="left:236px">
    <div class="icon"><svg width="28" height="28" viewBox="0 0 28 28" fill="none" stroke="#fff" stroke-width="2"><rect x="7" y="12" width="14" height="11" rx="2"/><path d="M10 12V9a4 4 0 0 1 8 0v3"/><circle cx="14" cy="17" r="1.5" fill="#fff"/></svg></div>
    <h3>Security</h3>
    <p>Morbi diam mauris viverra in gravida<br>eu mattis in ante Morbi eget arcu<br>Morbi porta libero ullam</p>
  </div>
  <div class="service" style="left:379px">
    <div class="icon"><svg width="30" height="28" viewBox="0 0 30 28" fill="none" stroke="#fff" stroke-width="3" stroke-linecap="round"><path d="M4 12a16 16 0 0 1 22 0"/><path d="M8.5 16.5a9.5 9.5 0 0 1 13 0"/><circle cx="15" cy="21" r="2" fill="#fff" stroke="none"/></svg></div>
    <h3>VoIP &amp; WiFi</h3>
    <p>Morbi diam mauris viverra in gravida<br>eu mattis in ante Morbi eget arcu<br>Morbi porta libero ullam</p>
  </div>
  <div class="service" style="left:522px">
    <div class="icon"><svg width="28" height="28" viewBox="0 0 28 28" fill="none" stroke="#fff" stroke-width="2.5" stroke-linecap="round"><path d="M7 21l9-9"/><path d="M16 12a4 4 0 1 1 4 4"/><path d="M8 7l13 13"/><path d="M6 6l3-1 1 3"/></svg></div>
    <h3>Testing &amp; Support</h3>
    <p>Morbi diam mauris viverra in gravida<br>eu mattis in ante Morbi eget arcu<br>Morbi porta libero ullam</p>
  </div>
</section>

<section class="cards">
  <article class="card" style="left:98px">
    <div class="photo" role="img" aria-label="Photo of a hand with connected technology icons" style="background:linear-gradient(90deg,#2f3338,#6a6e74)"></div>
    <h3>WHAT WE DO</h3>
    <p>Etiam est nunc venenatis in tristique eu imperdiet<br>ac nisl Cum sociis natoque penatibus et magnis<br>dis parturient montes nascetur ridicu</p>
  </article>
  <article class="card" style="left:285px">
    <div class="photo" role="img" aria-label="Photo of hands joining puzzle pieces" style="background:linear-gradient(90deg,#d8c9bb,#efe6dc)"></div>
    <h3>OUR SUPPORT</h3>
    <p>Etiam est nunc venenatis in tristique eu imperdiet<br>ac nisl Cum sociis natoque penatibus et magnis<br>dis parturient montes nascetur ridicu</p>
  </article>
  <article class="card" style="left:473px">
    <div class="photo" role="img" aria-label="Photo of a hand touching a digital globe" style="background:linear-gradient(90deg,#2d4f7d,#9bb6d4)"></div>
    <h3 style="margin-top:6px">PROJECTS</h3>
    <p>Etiam est nunc venenatis in tristique eu imperdiet<br>ac nisl Cum sociis natoque penatibus et magnis<br>dis parturient montes nascetur ridicu</p>
  </article>
</section>

<div class="map" role="img" aria-label="Street map of central London showing the office location"></div>
<div class="address">Unit 4 Harrow Court<br>18 Marsh Lane London<br>Greater London<br>SE1 7QX</div>
<svg class="pin" width="12" height="18" viewBox="0 0 12 18"><path d="M6 0a6 6 0 0 1 6 6c0 4-6 12-6 12S0 10 0 6a6 6 0 0 1 6-6z" fill="#d9342b"/><circle cx="6" cy="6" r="2" fill="#7a1410"/></svg>

<footer class="site-footer">
  <nav class="footer-nav"><a href="#">Home</a> &nbsp;|&nbsp; <a href="#">About us</a> &nbsp;|&nbsp; <a href="#">Services</a> &nbsp;|&nbsp; <a href="#">Clients</a> &nbsp;|&nbsp; <a href="#">Projects</a> &nbsp;|&nbsp; <a href="#">Contact</a></nav>
  <p class="copyright">© 2014 Company Name &nbsp;All right reserved &nbsp;Term of Use</p>
  <div class="social"><span></span><span></span><span></span></div>
</footer>
</body>
</html>
```